New business card for UK roofing company

We are Penwick Roofing and we need a business card design for our staff.

We offer the following services:

- New roofs
- General roof repairs
- Drone surveys
- Single ply roofing
- Steel cladding
- Asbestos removal
- Electronic leak detection

I have attached our logo. I have also attached example branding printed to our vans. The business card should fit in with the style of our branding.

The business card should have the following information;

Address:
Unit 17c Marlow Dene Farm
Marlow Dene Lane
Fenbury
RX4 9QD

Telephone: 020 7946 0312
24 Hour: 0800 471 9062

Email: tom@penwickroofing.com
Mobile: 07700900418
Name: Tom Harley
Website: www.penwickroofing.com

The business card will be printed in Spot UV, see here: https://www.printvane.com/business-cards/spot-uv/

If you need anymore info, please let me know,

```html
<!DOCTYPE html>
<html lang="en">
<head>
<meta charset="utf-8">
<title>Penwick Roofing – Business Card</title>
<link rel="stylesheet" href="https://fonts.googleapis.com/css2?family=Figtree:wght@400;800&display=swap">
<style>
  :root {
    --navy: #003da5;
    --deep: #0a3aa0;
    --cyan: #46eeea;
    --white: #ffffff;
    --stage: #d9d9d9;
  }
  * { margin: 0; padding: 0; box-sizing: border-box; }
  html, body { width: 1200px; height: 846px; overflow: hidden; }
  body {
    background: var(--stage);
    font-family: "Figtree", sans-serif;
    position: relative;
  }
  .card {
    position: absolute;
    left: 347px;
    width: 509px;
    height: 291px;
    overflow: hidden;
    background: var(--white);
  }
  .card--front { top: 99px; }
  .card--back { top: 457px; }

  .brand-name {
    position: absolute;
    font-weight: 800;
    font-size: 24px;
    letter-spacing: -0.6px;
    color: var(--navy);
    white-space: nowrap;
    line-height: 1;
  }
  .card--front .brand-name { left: 54px; top: 58px; }
  .card--back .brand-name { left: 34px; top: 247px; }

  .person-name {
    position: absolute;
    left: 54px; top: 126px;
    font-weight: 800;
    font-size: 19px;
    color: var(--navy);
  }
  .person-name .surname { color: var(--cyan); }

  .contact {
    position: absolute;
    font-size: 14px;
    line-height: 17px;
    color: var(--navy);
    white-space: nowrap;
  }
  .contact .label { font-weight: 800; color: var(--cyan); }
  .contact--phones { left: 54px; top: 166px; }
  .contact--online { left: 243px; top: 183px; }

  .rule {
    position: absolute;
    left: 54px; top: 229px;
    width: 399px; height: 1px;
    background: var(--cyan);
  }
  .address {
    position: absolute;
    left: 54px; top: 239px;
    font-size: 14px;
    color: var(--navy);
    white-space: nowrap;
  }

  .back-art { position: absolute; left: 0; top: 0; }

  .hotline {
    position: absolute;
    left: 34px; top: 26px;
    display: flex; align-items: center; gap: 6px;
  }
  .hotline-number {
    font-weight: 800;
    font-size: 20px;
    color: var(--white);
    letter-spacing: 0.3px;
  }
  .services {
    position: absolute;
    left: 36px; top: 80px;
    list-style: none;
    font-weight: 800;
    font-size: 11.5px;
    line-height: 16.2px;
    color: var(--white);
    letter-spacing: 0.3px;
  }
  .services li::before { content: "• "; }
</style>
</head>
<body>

<section class="card card--front" aria-label="Business card front">
  <div class="brand-name">Penwick Roofing</div>
  <h1 class="person-name">Tom <span class="surname">Harley</span></h1>
  <div class="contact contact--phones">
    <div><span class="label">Mobile:</span> 077 0090 0418</div>
    <div><span class="label">Telephone:</span> 020 7946 0312</div>
    <div><span class="label">24 Hour:</span> 0800 471 9062</div>
  </div>
  <div class="contact contact--online">
    <div><span class="label">Email:</span> tom@penwickroofing.com</div>
    <div><span class="label">Website:</span> www.penwickroofing.com</div>
  </div>
  <div class="rule"></div>
  <p class="address">Unit 17c Marlow Dene Farm, Marlow Dene Lane, Fenbury RX4 9QD</p>
</section>

<section class="card card--back" aria-label="Business card back">
  <svg class="back-art" width="509" height="291" viewBox="0 0 509 291">
    <polygon points="0,0 509,0 509,75 0,229" fill="var(--navy)"/>
    <polygon points="0,229 509,75 509,85 0,239" fill="var(--cyan)"/>
    <circle cx="370" cy="150" r="135" fill="var(--white)" stroke="var(--navy)" stroke-width="3"/>
  </svg>

  <div class="hotline">
    <svg width="44" height="44" viewBox="0 0 44 44" aria-hidden="true">
      <path d="M36 9 A19 19 0 1 0 30 39" fill="none" stroke="var(--white)" stroke-width="2"/>
      <path d="M39 17 A19 19 0 0 1 33 37" fill="none" stroke="var(--white)" stroke-width="2" stroke-dasharray="3 3"/>
      <polygon points="33,4 40,8 33,12" fill="var(--white)"/>
      <text x="21" y="22" text-anchor="middle" font-family="Figtree, sans-serif" font-weight="800" font-size="11" fill="var(--white)">24/7</text>
      <text x="21" y="30" text-anchor="middle" font-family="Figtree, sans-serif" font-weight="800" font-size="6" fill="var(--white)">SERVICE</text>
    </svg>
    <span class="hotline-number">0800 471 9062</span>
  </div>

  <ul class="services">
    <li>General Roof Repairs</li>
    <li>Drone Roof Surveys</li>
    <li>Single Ply Roofing</li>
    <li>Asbestos Removal</li>
    <li>Steel Cladding</li>
    <li>New Roofs</li>
  </ul>

  <div class="brand-name">Penwick Roofing</div>
</section>

</body>
</html>
```